Redesign for Popular UK Town Website

We're looking for someone to redesign a website for a popular tourist town that's visited by over 250,000 people a year. We have a basic design frame in place and need someone to make it look more 'professional.'
We've created a temporary design layout to show you a general idea of what we're looking for: http://quillhaven.co.uk/
All text/images are placeholder images so you can get an idea of the general layout.
(Please note that you can grab any images found on the internet for 'tenby' to be used as placeholder images. This is because we will be visiting the locations and taking our own photos, after the design is complete.)
Target Market(s)
Tourists
Industry/Entity Type
Town
Number of Pages Required
2 page
Requirements
Must have
- You need to redesign the homepage: http://quillhaven.co.uk/
- You also need to redesign the following page: http://quillhaven.co.uk/hotels/ (This page will be used for multiple categories and is used to list locations of properties/places etc.)
- Design must be responsive also.
Nice to have
- Please feel free to add as much as you can to the content/features as with our limited knowledge of websites, have only been able to create a basic layout.

```html
<!DOCTYPE html>
<html lang="en">
<head>
<meta charset="utf-8">
<title>Harbourline – Hotels in Quillhaven</title>
<link rel="stylesheet" href="https://fonts.googleapis.com/css2?family=Lato:wght@400;700;900&family=Squada+One&display=swap">
<style>
:root{
  --navy:#0d3b66;
  --topbar:#2c4a72;
  --sky:#1aa3e8;
  --ink:#1b1b1b;
  --grey-text:#555;
  --nav-grey:#555;
  --panel:#ececec;
  --white:#fff;
  --line:#e3e3e3;
}
*{box-sizing:border-box;margin:0;padding:0}
html,body{width:1200px;height:2521px;overflow:hidden;background:var(--white);font-family:"Lato",sans-serif;color:var(--ink)}
.page{position:relative;width:1200px;height:2521px}
.abs{position:absolute}

/* top bar */
.topbar{left:0;top:0;width:1200px;height:42px;background:linear-gradient(90deg,#2a466d,#34557f 50%,#2a466d)}
.social-top{left:88px;top:12px;display:flex;gap:30px}
.social-top span{width:16px;height:16px;border-radius:50%;background:rgba(255,255,255,.8);display:block}
.search{left:387px;top:5px;width:427px;height:32px;border-radius:16px;background:var(--sky);color:#fff;font-size:13px;padding:0 0 0 20px;line-height:32px}
.search svg{position:absolute;right:14px;top:7px}
.contact-link{left:995px;top:6px;color:#fff;font-size:23px;text-decoration:underline;text-underline-offset:3px}
.contact-link b{text-decoration:none;display:inline-block;margin-left:6px;font-weight:700}

/* nav */
.header{left:0;top:42px;width:1200px;height:93px;background:#fff}
.brand{left:77px;top:22px;display:flex;align-items:center;gap:10px}
.brand-mark{width:48px;height:48px;border-radius:50%;background:var(--navy)}
.brand-name{font-weight:900;font-size:26px;color:var(--navy)}
.nav{left:0;top:0;width:1200px;height:93px}
.nav-item{position:absolute;top:15px;font-size:15px;color:var(--nav-grey);text-align:center;white-space:nowrap;transform:translateX(-50%)}
.nav-item svg{display:block;margin:0 auto 6px}
.nav-item.is-active{color:var(--sky)}

/* hero */
.hero{left:0;top:135px;width:1200px;height:542px;background:linear-gradient(160deg,#8fa6b4 0%,#b7b7a8 30%,#7f96a0 55%,#a6a49a 80%,#c8c0b0 100%)}
.hero-title{left:79px;top:318px;font-size:51px;font-weight:900;color:var(--navy);line-height:1}
.hero-sub{left:79px;top:378px;font-size:31px;font-weight:900;color:#111;display:flex;align-items:center;gap:8px}
.hero-text{left:79px;top:423px;width:440px;font-size:13px;line-height:19px;color:#111}

/* discover */
.discover{left:77px;top:593px;width:701px;height:367px;background:var(--panel)}
.discover-card{left:99px;top:615px;width:656px;height:323px;background:#fff;box-shadow:0 4px 14px rgba(0,0,0,.18)}
.discover-title{left:151px;top:682px;font-family:"Squada One",sans-serif;font-size:40px;letter-spacing:4px;color:#111}
.discover-text{left:151px;top:742px;width:540px;font-size:13.5px;line-height:23px;color:var(--grey-text)}
.btn{background:var(--sky);color:#fff;border-radius:24px;text-align:center;font-weight:400}
.discover-btn{left:151px;top:829px;width:259px;height:45px;line-height:45px;font-size:18px}

/* hotel cards */
.hotel{overflow:hidden;color:#fff}
.hotel-frame{position:absolute;left:17px;top:17px;right:17px;bottom:17px;border:1px solid rgba(255,255,255,.85)}
.hotel-name{position:absolute;left:0;right:0;top:94px;text-align:center;font-family:"Squada One",sans-serif;font-size:39px;line-height:44px}
.hotel-info{position:absolute;left:10px;right:10px;top:178px;list-style:none;text-align:center;font-size:16px;line-height:31px}
.hotel-info li{white-space:nowrap}
.hotel-info svg{vertical-align:-2px;margin-right:8px}
.hotel-info .wrap{white-space:normal;line-height:19px;padding-top:6px}
.hotel.featured .hotel-name{top:82px;font-size:44px}
.featured-rule{position:absolute;left:40px;right:24px;top:154px;height:1px;background:rgba(255,255,255,.8)}
.hotel.featured .hotel-info{top:170px}
.more{position:absolute;left:155px;top:298px;width:44px;height:44px;border-radius:50%;background:#fff}
.tone-a{background:linear-gradient(180deg,#3a5f86,#264a70)}
.tone-b{background:linear-gradient(180deg,#2f5377,#1f3d5c)}
.tone-c{background:linear-gradient(180deg,#4a5a6a,#2a3440)}
.tone-d{background:linear-gradient(180deg,#3b4a5c,#1e2832)}
.tone-e{background:linear-gradient(180deg,#4d6f92,#2d5074)}
.tone-f{background:linear-gradient(180deg,#5b5a52,#2e3a44)}
.tone-g{background:linear-gradient(180deg,#3f6690,#284d74)}
.tone-h{background:linear-gradient(180deg,#39485c,#202c38)}
.tone-i{background:linear-gradient(180deg,#2e587f,#1c3c5c)}

/* footer */
.load-more{left:506px;top:2131px;width:188px;height:51px;line-height:51px;font-size:19px;border-radius:26px}
.divider{left:77px;top:2219px;width:1046px;height:1px;background:var(--line)}
.footer-brand{left:0;top:2268px;width:1200px;display:flex;flex-direction:column;align-items:center;gap:14px}
.footer-brand .brand-mark{width:80px;height:80px}
.footer-brand .brand-name{font-size:34px}
.footer-social{left:0;top:2419px;width:1200px;display:flex;justify-content:center;gap:16px}
.footer-social span{width:36px;height:36px;border-radius:50%;border:2px solid var(--navy);display:block}
.copyright{left:0;top:2479px;width:1200px;text-align:center;font-size:13.5px;color:var(--grey-text)}
.copyright b{color:var(--navy)}
</style>
</head>
<body>
<svg width="0" height="0" style="position:absolute">
  <symbol id="i-phone" viewBox="0 0 16 16"><path fill="currentColor" d="M3.6 1.2l2.2 2.6-1.2 1.8c.9 2 2.6 3.7 4.6 4.6l1.8-1.2 2.6 2.2-1.2 2.4C7.6 13.6 2.4 8.4 1.2 3z"/></symbol>
  <symbol id="i-mail" viewBox="0 0 16 16"><path fill="currentColor" d="M1 3h14v10H1z"/><path fill="none" stroke="#2a4a6c" stroke-width="1.3" d="M1 3.5l7 5 7-5"/></symbol>
  <symbol id="i-web" viewBox="0 0 16 16"><circle cx="8" cy="8" r="7" fill="currentColor"/><path fill="none" stroke="#2a4a6c" stroke-width="1" d="M1 8h14M8 1c-3 3-3 11 0 14M8 1c3 3 3 11 0 14"/></symbol>
</svg>

<div class="page">
  <div class="abs topbar">
    <div class="abs social-top"><span></span><span></span><span></span></div>
    <div class="abs search">Search...
      <svg width="18" height="18" viewBox="0 0 18 18"><circle cx="7.5" cy="7.5" r="5.5" fill="none" stroke="#fff" stroke-width="2"/><path d="M11.5 11.5l5 5" stroke="#fff" stroke-width="2.4"/></svg>
    </div>
    <div class="abs contact-link">Contact Us<b>»</b></div>
  </div>

  <header class="abs header">
    <div class="abs brand"><span class="brand-mark"></span><span class="brand-name">Harbourline</span></div>
    <nav class="abs nav">
      <div class="nav-item is-active" style="left:396px"><svg width="20" height="18" viewBox="0 0 20 18"><path fill="currentColor" d="M10 1L1 9h3v8h4v-5h4v5h4V9h3z"/></svg>HOME</div>
      <div class="nav-item" style="left:511px"><svg width="20" height="18" viewBox="0 0 20 18"><path fill="#c9c9c9" d="M9 1h2v5l7 4v2l-7-2v4l2 2v1l-3-1-3 1v-1l2-2v-4l-7 2v-2l7-4z"/></svg>WHERE TO STAY</div>
      <div class="nav-item" style="left:689px"><svg width="26" height="18" viewBox="0 0 26 18"><path fill="#c9c9c9" d="M2 3h18l3 6v5H2z"/><circle cx="8" cy="15" r="2.5" fill="#999"/></svg>CARVAN AND CAMPING</div>
      <div class="nav-item" style="left:885px"><svg width="24" height="18" viewBox="0 0 24 18"><path fill="#c9c9c9" d="M2 3h2v7h18v6h-2v-3H4v3H2zM5 6h6v4H5z"/></svg>BED AND BREAKFAST</div>
      <div class="nav-item" style="left:1060px"><svg width="18" height="18" viewBox="0 0 18 18"><path fill="#c9c9c9" d="M3 2h12v15H3z"/></svg>HOTELS IN QUILLHAVEN</div>
    </nav>
  </header>

  <section class="abs hero" role="img" aria-label="Aerial photograph of the harbour town with coloured houses and moored boats"></section>
  <h1 class="abs hero-title">HOTELS</h1>
  <div class="abs hero-sub">WE PROVIDE BEST
    <svg width="26" height="26" viewBox="0 0 26 26"><circle cx="13" cy="13" r="12" fill="#333"/><path fill="none" stroke="#bbb" stroke-width="1.4" d="M1 13h24M13 1c-5 5-5 19 0 24M13 1c5 5 5 19 0 24"/></svg>
    QUALITY...</div>
  <p class="abs hero-text">Lorem Ipsum is simply dummy text of the printing and typesetting industry. Lorem Ipsum has been the industry's standard dummy text.</p>

  <div class="abs discover"></div>
  <div class="abs discover-card"></div>
  <h2 class="abs discover-title">DISCOVER HOTEL</h2>
  <p class="abs discover-text">Most famous for it's Gullcrest Hotel, Quillhaven actually has over 18 hotels with availability throughout the year. All information for the hotels listed below are valid as of March 2018. To make a booking enquiry, please contact the hotels directly.</p>
  <div class="abs btn discover-btn">SEE IT! FEEL IT! LOVE IT!</div>

  <article class="abs hotel featured tone-a" style="left:785px;top:593px;width:338px;height:367px" role="img" aria-label="Photograph of the Gullcrest Hotel façade under a blue overlay">
    <h3 class="hotel-name">Gullcrest Hotel</h3>
    <div class="featured-rule"></div>
    <ul class="hotel-info" style="color:#fff">
      <li><svg width="15" height="15" style="color:#ddd"><use href="#i-phone"/></svg>01632 960480</li>
      <li><svg width="15" height="15" style="color:#ddd"><use href="#i-mail"/></svg>stay@gullcresthotel.co.uk</li>
      <li><svg width="15" height="15" style="color:#ddd"><use href="#i-web"/></svg>http://www.gullcresthotel.co.uk/</li>
    </ul>
    <div class="more"><svg width="44" height="44"><path d="M22 12v20M12 22h20" stroke="#1b2d40" stroke-width="2.5"/></svg></div>
  </article>

  <article class="abs hotel tone-b" style="left:77px;top:968px;width:338px;height:363px" role="img" aria-label="Photograph of The Meadow Hotel entrance">
    <div class="hotel-frame"></div>
    <h3 class="hotel-name">The Meadow Hotel</h3>
    <ul class="hotel-info">
      <li><svg width="15" height="15" style="color:#ddd"><use href="#i-phone"/></svg>01632 960480</li>
      <li><svg width="15" height="15" style="color:#ddd"><use href="#i-mail"/></svg>desk@meadowhotelqh.com</li>
      <li><svg width="15" height="15" style="color:#ddd"><use href="#i-web"/></svg>http://meadowhotelqh.com/</li>
    </ul>
  </article>

  <article class="abs hotel tone-c" style="left:420px;top:968px;width:703px;height:363px" role="img" aria-label="Photograph of The Harbour View Hotel terrace at dusk">
    <div class="hotel-frame"></div>
    <h3 class="hotel-name" style="top:80px">The Harbour View Hotel</h3>
    <ul class="hotel-info" style="top:164px">
      <li><svg width="15" height="15" style="color:#ddd"><use href="#i-phone"/></svg>01632 960480</li>
      <li><svg width="15" height="15" style="color:#ddd"><use href="#i-web"/></svg>http://www.theharbourviewhotel.com/</li>
    </ul>
  </article>

  <article class="abs hotel tone-d" style="left:77px;top:1341px;width:338px;height:364px" role="img" aria-label="Photograph of Sandmere House Hotel">
    <div class="hotel-frame"></div>
    <h3 class="hotel-name">Sandmere House Hotel</h3>
    <ul class="hotel-info">
      <li><svg width="15" height="15" style="color:#ddd"><use href="#i-phone"/></svg>01632 960371</li>
      <li><svg width="15" height="15" style="color:#ddd"><use href="#i-mail"/></svg>info@sandmerehouse-qh.co.uk</li>
      <li class="wrap"><svg width="15" height="15" style="color:#ddd"><use href="#i-web"/></svg>https://www.sandmerehouse-<br>qh.co.uk/</li>
    </ul>
  </article>

  <article class="abs hotel tone-e" style="left:430px;top:1341px;width:338px;height:364px" role="img" aria-label="Photograph of The Kestrel Hotel">
    <div class="hotel-frame"></div>
    <h3 class="hotel-name">The Kestrel Hotel</h3>
    <ul class="hotel-info">
      <li><svg width="15" height="15" style="color:#ddd"><use href="#i-phone"/></svg>01632 960698</li>
      <li><svg width="15" height="15" style="color:#ddd"><use href="#i-mail"/></svg>kestrelhotelqh@mailbox.com</li>
      <li><svg width="15" height="15" style="color:#ddd"><use href="#i-web"/></svg>http://thekestrelhotelqh.com/</li>
    </ul>
  </article>

  <article class="abs hotel tone-f" style="left:783px;top:1341px;width:338px;height:364px" role="img" aria-label="Photograph of Tidewater Hotel">
    <div class="hotel-frame"></div>
    <h3 class="hotel-name">Tidewater Hotel</h3>
    <ul class="hotel-info">
      <li><svg width="15" height="15" style="color:#ddd"><use href="#i-phone"/></svg>01632 960881</li>
      <li><svg width="15" height="15" style="color:#ddd"><use href="#i-mail"/></svg>enquiries@tidewater-hotel.uk.com</li>
      <li><svg width="15" height="15" style="color:#ddd"><use href="#i-web"/></svg>http://www.tidewater-hotel.uk.com/</li>
    </ul>
  </article>

  <article class="abs hotel tone-g" style="left:77px;top:1715px;width:338px;height:363px" role="img" aria-label="Photograph of Seaholly Hotel">
    <div class="hotel-frame"></div>
    <h3 class="hotel-name">Seaholly Hotel</h3>
    <ul class="hotel-info">
      <li><svg width="15" height="15" style="color:#ddd"><use href="#i-phone"/></svg>01632 960377</li>
      <li><svg width="15" height="15" style="color:#ddd"><use href="#i-mail"/></svg>info@theseahollyhotel.co.uk</li>
      <li><svg width="15" height="15" style="color:#ddd"><use href="#i-web"/></svg>http://www.theseahollyhotel.co.uk</li>
    </ul>
  </article>

  <article class="abs hotel tone-h" style="left:430px;top:1715px;width:338px;height:363px" role="img" aria-label="Photograph of Lantern Hotel">
    <div class="hotel-frame"></div>
    <h3 class="hotel-name">Lantern Hotel</h3>
    <ul class="hotel-info">
      <li><svg width="15" height="15" style="color:#ddd"><use href="#i-phone"/></svg>01632 960760</li>
      <li><svg width="15" height="15" style="color:#ddd"><use href="#i-mail"/></svg>lanternquillhaven@mailbox.com</li>
      <li><svg width="15" height="15" style="color:#ddd"><use href="#i-web"/></svg>http://www.lanternquillhaven.co.uk/</li>
    </ul>
  </article>

  <article class="abs hotel tone-i" style="left:783px;top:1715px;width:338px;height:363px" role="img" aria-label="Photograph of Driftwood Hotel">
    <div class="hotel-frame"></div>
    <h3 class="hotel-name">Driftwood Hotel</h3>
    <ul class="hotel-info">
      <li><svg width="15" height="15" style="color:#ddd"><use href="#i-phone"/></svg>01632 960436</li>
      <li><svg width="15" height="15" style="color:#ddd"><use href="#i-mail"/></svg>driftwoodhotel@mailbox.com</li>
      <li class="wrap"><svg width="15" height="15" style="color:#ddd"><use href="#i-web"/></svg>http://www.driftwoodhotel-qh.co.<br>uk/</li>
    </ul>
  </article>

  <div class="abs btn load-more">Load More</div>
  <div class="abs divider"></div>

  <footer>
    <div class="abs footer-brand"><span class="brand-mark"></span><span class="brand-name">Harbourline</span></div>
    <div class="abs footer-social"><span></span><span></span><span></span></div>
    <p class="abs copyright">© <b>Harbourline</b> - 2016. All Rights Reserved.</p>
  </footer>
</div>
</body>
</html>
```